WordPress Website Design Project

Technical & Functional Deliverables
WordPress CMS
Fully responsive design
Integrated WhatsApp chatbot
Custom article filtering system
SEO-friendly site structure & performance optimization
CMS user manual & training session

Industry/Entity Type

Industrial Safety and Compliance

Coding

Coded - Design and coding required

Number of Pages Required

5+ page

Font styles to use
Sans Serif

Colors
0054AA
0677BA
7BADD7
CADEEF
E8F1F8

```html
<!DOCTYPE html>
<html lang="en">
<head>
<meta charset="utf-8">
<title>Halvard — Your Partner In Industrial Safety &amp; Compliance</title>
<link href="https://fonts.googleapis.com/css2?family=Montserrat:wght@400;600;700;800&family=Poppins:wght@300;400;500;600&display=swap" rel="stylesheet">
<style>
:root{
  --navy:#1c2c4c;
  --navy-deep:#16233e;
  --blue:#0054AA;
  --blue-mid:#0677BA;
  --blue-soft:#7BADD7;
  --blue-pale:#CADEEF;
  --blue-mist:#E8F1F8;
  --ink:#1b1f2a;
  --grey:#6b7280;
  --ghost:#eceff3;
  --white:#ffffff;
}
*{margin:0;padding:0;box-sizing:border-box}
html,body{width:1200px;height:5140px;overflow:hidden;background:var(--white)}
body{font-family:"Poppins",sans-serif;color:var(--ink);position:relative}
.abs{position:absolute}
.ph{position:absolute;border-radius:14px}

/* hero */
.hero{position:absolute;left:0;top:0;width:1200px;height:650px;
  background:linear-gradient(180deg,#24365a 0%,var(--navy) 60%,var(--navy-deep) 100%);overflow:hidden}
.hero-bg{position:absolute;inset:0;background:linear-gradient(120deg,rgba(60,80,115,.5),rgba(28,44,76,0) 60%)}
.brand{position:absolute;left:60px;top:18px;color:var(--white)}
.brand-name{font-family:"Montserrat",sans-serif;font-weight:800;font-size:34px;letter-spacing:3px;display:flex;align-items:center;gap:10px}
.brand-name .mark{width:30px;height:30px;background:var(--blue-soft)}
.brand-tag{font-size:9.5px;letter-spacing:.6px;font-weight:500;margin-top:2px;text-transform:uppercase}
.nav{position:absolute;right:70px;top:46px;display:flex;gap:28px;color:var(--white);font-size:14px}
.hero h1{position:absolute;left:100px;top:225px;width:420px;color:var(--white);font-family:"Poppins",sans-serif;font-weight:500;font-size:42px;line-height:1.2}
.btn{position:absolute;left:100px;top:393px;width:190px;height:54px;border-radius:27px;background:var(--blue-mid);color:var(--white);font-size:16px;display:flex;align-items:center;justify-content:center}
.hero-photo{left:545px;top:160px;width:575px;height:375px;border-radius:22px;background:linear-gradient(135deg,#c9d4e2,#8fa3bd 55%,#5d708d)}
.dots{position:absolute;display:flex;gap:10px}
.dots i{width:10px;height:10px;border-radius:50%;border:1.5px solid var(--blue-soft);display:block}
.dots i.on{background:var(--blue-soft)}

/* section headings */
.ghost-word{position:absolute;left:0;width:1200px;text-align:center;font-family:"Montserrat",sans-serif;font-weight:800;color:var(--ghost);font-size:96px;letter-spacing:4px}
.sec-title{position:absolute;left:0;width:1200px;text-align:center;font-family:"Montserrat",sans-serif;font-weight:800;font-size:48px;letter-spacing:-.5px;color:var(--ink)}

/* about */
.about-photo{left:60px;top:835px;width:505px;height:425px;border-radius:26px;background:linear-gradient(135deg,#dfe7f0,#a9b7c8 50%,#6b7c93)}
.about-text{position:absolute;left:605px;top:880px;width:560px}
.about-text h2{font-weight:400;font-size:32px;line-height:1.2;color:var(--blue)}
.about-text h3{font-weight:400;font-size:20px;color:var(--blue-mid);margin-top:22px}
.about-text p{font-size:13px;line-height:1.5;color:var(--grey);margin-top:16px;width:470px}
.about-text .lead{font-size:28px;color:var(--blue-mid);line-height:1.2;margin-top:22px;width:520px}
.wordmark{position:absolute;left:0;top:1345px;width:1200px;text-align:center;font-family:"Poppins",sans-serif;font-weight:200;font-size:170px;letter-spacing:34px;color:#d6d9de}

/* values */
.value{position:absolute;width:240px;height:200px;border-radius:12px;background:var(--blue-mist);text-align:center;padding:40px 22px}
.value h4{font-weight:500;font-size:20px;color:var(--ink)}
.value p{font-size:13px;line-height:1.45;color:var(--grey);margin-top:8px}
.value.active{background:var(--blue-soft)}
.value.active h4,.value.active p{color:var(--white)}
.values-photo{left:620px;top:1800px;width:500px;height:205px;background:linear-gradient(120deg,#f1f5fa,#c6d3e2 60%,#8ea2bb)}

/* work */
.work-photo{top:2250px;width:340px;height:480px;border-radius:16px}

/* clients */
.client{position:absolute;width:180px;height:90px;border-radius:8px;background:var(--white);box-shadow:0 2px 10px rgba(20,40,70,.12);display:flex;align-items:center;justify-content:center;gap:8px;font-weight:600;font-size:22px;color:var(--blue)}
.client b{width:14px;height:14px;border-radius:50%;background:var(--blue-soft);display:block}

/* solutions */
.solution{position:absolute;top:3480px;width:250px}
.solution h5{font-weight:500;font-size:16px;line-height:1.3;height:58px;color:var(--ink)}
.solution .ph{position:relative;display:block;width:250px;height:410px;border-radius:6px}

/* people */
.people-intro{position:absolute;left:330px;top:4072px;width:540px;text-align:center;font-size:12.5px;line-height:1.55;color:var(--grey)}
.person{position:absolute;top:4180px;width:215px}
.person .ph{position:relative;display:block;width:215px;height:300px;border-radius:12px}
.person h6{font-weight:500;font-size:19px;margin-top:14px;color:var(--ink)}
.person span{display:block;font-size:11px;color:var(--grey);margin-top:2px}
.person p{font-size:10.5px;line-height:1.45;color:var(--grey);margin-top:10px;width:200px}

/* footer */
.footer{position:absolute;left:0;top:4740px;width:1200px;height:400px;background:var(--navy);color:var(--white)}
.footer h2{position:absolute;left:100px;top:180px;font-weight:400;font-size:28px;line-height:1.25;width:420px}
.foot-rule{position:absolute;left:540px;top:150px;width:1px;height:150px;background:rgba(255,255,255,.35)}
.foot-col{position:absolute;top:158px;font-size:13px;line-height:1.65}
.foot-rule2{position:absolute;left:660px;top:150px;width:1px;height:150px;background:rgba(255,255,255,.35)}
.foot-bottom{position:absolute;left:100px;top:360px;font-size:13px}
.social{position:absolute;left:100px;top:380px;font-weight:600;font-size:20px;display:flex;align-items:center;gap:8px}
.social b{width:14px;height:14px;background:var(--blue-soft);display:block}
.copyright{position:absolute;left:650px;top:370px;font-size:12px}
.foot-brand{left:885px;top:320px}
</style>
</head>
<body>

<header class="hero">
  <div class="hero-bg" role="img" aria-label="Industrial plant backdrop in deep navy tones"></div>
  <div class="brand">
    <div class="brand-name"><span class="mark"></span>HALVARD</div>
    <div class="brand-tag">Your partner in industrial<br>safety and compliance</div>
  </div>
  <nav class="nav"><span>Home</span><span>About Us</span><span>Solutions</span><span>Articles</span><span>Contact Us</span></nav>
  <h1>Your Partner In Industrial Safety &amp; Compliance</h1>
  <div class="btn">Contact us</div>
  <div class="ph hero-photo" role="img" aria-label="Team of engineers reviewing plans around a table"></div>
  <div class="dots" style="left:800px;top:540px"><i class="on"></i><i></i><i></i><i></i><i></i></div>
</header>

<div class="ghost-word" style="top:655px">VALUES</div>
<div class="sec-title" style="top:705px">OUR VALUES</div>

<div class="ph about-photo" role="img" aria-label="Colleagues working together at a laptop"></div>
<div class="about-text">
  <h2>We are Halvard:<br>Your Partner in Industrial Safety and Compliance</h2>
  <h3>Mission Statement And Core Values</h3>
  <p>To Provide Expert Guidance And Practical Solutions In Industrial Safety And Compliance, Delivering Clarity, Reliability, And Peace Of Mind To Every Partner We Serve.</p>
  <div class="lead">We achieve this mission by staying true to our foundational values:</div>
</div>
<div class="wordmark">HALVARD</div>

<div class="value" style="left:100px;top:1560px"><h4>Assurance</h4><p>Providing Confidence Through Technically Robust Solutions.</p></div>
<div class="value active" style="left:360px;top:1560px"><h4>Reliability</h4><p>Ensuring consistent performance in demanding situations.</p></div>
<div class="value" style="left:620px;top:1560px"><h4>Commitment</h4><p>Fulfilling Promises And Exceeding Expectations.</p></div>
<div class="value" style="left:880px;top:1560px"><h4>Honor</h4><p>Upholding The Highest Ethical Standards.</p></div>
<div class="value" style="left:100px;top:1805px"><h4>Expertise</h4><p>Leveraging Deep Industry Knowledge To Solve Complex Challenges.</p></div>
<div class="value" style="left:360px;top:1805px"><h4>Responsibility</h4><p>Taking Full Accountability From Concept Through Completion.</p></div>
<div class="ph values-photo" role="img" aria-label="Rolled engineering drawings on a desk"></div>

<div class="ghost-word" style="top:2055px">WORK</div>
<div class="sec-title" style="top:2105px">OUR WORK</div>
<div class="ph work-photo" style="left:60px;background:linear-gradient(180deg,#b8cde2,#7f95ad 60%,#50627a)" role="img" aria-label="Refinery towers and pipework"></div>
<div class="ph work-photo" style="left:430px;background:linear-gradient(160deg,#5a93c9,#d9a24a 55%,#6a5a3e)" role="img" aria-label="Construction worker with crane and rebar"></div>
<div class="ph work-photo" style="left:800px;background:linear-gradient(180deg,#9fb4c8,#7a8796 55%,#4a5563)" role="img" aria-label="Industrial plant under a cloudy sky"></div>
<div class="dots" style="left:533px;top:2755px"><i class="on"></i><i></i><i></i><i></i><i></i></div>

<div class="sec-title" style="top:2850px">OUR CLIENTS</div>
<div class="client" style="left:60px;top:2995px"><b></b>Corvane</div>
<div class="client" style="left:280px;top:2995px"><b></b>Lumeris</div>
<div class="client" style="left:500px;top:2995px"><b></b>Norvik</div>
<div class="client" style="left:720px;top:2995px"><b></b>Basalt Vaults</div>
<div class="client" style="left:940px;top:2995px"><b></b>Straitline Air</div>
<div class="client" style="left:60px;top:3135px"><b></b>Pellion</div>
<div class="client" style="left:280px;top:3135px"><b></b>Harbora</div>
<div class="client" style="left:500px;top:3135px"><b></b>Polyvent</div>
<div class="client" style="left:720px;top:3135px"><b></b>Quarral</div>
<div class="client" style="left:940px;top:3135px"><b></b>Tessaro</div>

<div class="ghost-word" style="top:3255px">SOLUTIONS</div>
<div class="sec-title" style="top:3305px">OUR SOLUTIONS</div>
<div class="solution" style="left:55px"><h5>Engineering &amp; Design</h5><span class="ph" style="background:linear-gradient(160deg,#eef2f6,#c8cfd8 55%,#d9b04a)" role="img" aria-label="Drawings, hard hat and tools on a desk"></span></div>
<div class="solution" style="left:335px"><h5>Technical Support &amp; Site Services</h5><span class="ph" style="background:linear-gradient(160deg,#dfe6ee,#9eb0c4 55%,#5d6f86)" role="img" aria-label="Technician with laptop in a facility"></span></div>
<div class="solution" style="left:615px"><h5>Risk Management &amp; Compliance Services</h5><span class="ph" style="background:linear-gradient(160deg,#c9d3de,#8a8f86 55%,#e0a040)" role="img" aria-label="Engineer in hard hat reviewing a site"></span></div>
<div class="solution" style="left:895px"><h5>Transitioning To Fluorine-Free Foam</h5><span class="ph" style="background:linear-gradient(180deg,#cfdceb,#9aa9b8 55%,#6e7b89)" role="img" aria-label="Rows of storage containers"></span></div>

<div class="ghost-word" style="top:3955px">PEOPLE</div>
<div class="sec-title" style="top:4000px">OUR PEOPLE</div>
<p class="people-intro">The Point Of Using Lorem Ipsum Is That It Has A More-Or-Less Normal Distribution Of Letters, As Opposed To Using 'Content Here, Content Here', Making It Look Like Readable English.</p>

<div class="person" style="left:20px"><span class="ph" style="background:linear-gradient(180deg,#e3e8ee,#9aa6b4)" role="img" aria-label="Portrait of Maren Holt"></span><h6>Maren Holt</h6><span>Mechanical Engineer</span><p>Leads plant integrity reviews and guides teams through safety audits, design checks and on-site hazard assessments for clients.</p></div>
<div class="person" style="left:255px"><span class="ph" style="background:linear-gradient(180deg,#e6ebf0,#a3adb9)" role="img" aria-label="Portrait of Maren Holt"></span><h6>Maren Holt</h6><span>Mechanical Engineer</span></div>
<div class="person" style="left:490px"><span class="ph" style="background:linear-gradient(180deg,#e1e6ec,#98a3b0)" role="img" aria-label="Portrait of Daniel Reyes"></span><h6>Daniel Reyes</h6><span>Mechanical Engineer</span></div>
<div class="person" style="left:725px"><span class="ph" style="background:linear-gradient(180deg,#e5e9ee,#a0aab6)" role="img" aria-label="Portrait of Lina Tan"></span><h6>Lina Tan</h6><span>Residence Engineer</span></div>
<div class="person" style="left:960px"><span class="ph" style="background:linear-gradient(180deg,#e2e7ed,#9ba6b3)" role="img" aria-label="Portrait of Tomas Varga"></span><h6>Tomas Varga</h6><span>Structural Engineer</span></div>

<footer class="footer">
  <h2>We Are Halvard.<br>Your Partner In Industrial Safety And Compliance</h2>
  <div class="foot-rule"></div>
  <div class="foot-col" style="left:560px">Home<br>About Us<br>Solutions<br>Contact Us<br>Articles</div>
  <div class="foot-rule2"></div>
  <div class="foot-col" style="left:680px">Engineering &amp; Design<br>Technical Support &amp; Site Services<br>Risk Management &amp; Compliance Services<br>Transitioning To Fluorine-Free Foam</div>
  <div class="foot-bottom" style="top:338px">Legal | Cookies | Privacy</div>
  <div class="social" style="top:365px"><b></b>Netwise</div>
  <div class="copyright">(C) Halvard (S) Pte Ltd 2025</div>
  <div class="brand foot-brand">
    <div class="brand-name"><span class="mark"></span>HALVARD</div>
    <div class="brand-tag">Your partner in industrial<br>safety and compliance</div>
  </div>
</footer>

</body>
</html>
```